Southport Billboard for Hiring more CDL drivers

I need a catch design for a bill board (size 10ft by 36 ft) to catch the attention for semi truck drivers.
In the design I want it to include:
-My company logo along with my website(ridgewaycarriers.com) and my number(803-555-0172) for contact info.
-I also need it to say earn up to $90,000 a year
-I will send a few photos to choose from
-I need the logo to look clean and simple! I don't want it to be cluttered just clean, simple and catchy.!

Target Market(s)

CDL Class A holders
Semi Truck Drivers

Industry/Entity Type

Trucking Company

Font styles to use
Other font styles liked:
• a font to match my logo

Requirements
Must have
• "Make up to $90,000"
"ridgewaycarriers.com"
"803-555-0172"

```html
<!DOCTYPE html>
<html lang="en">
<head>
<meta charset="utf-8">
<title>Ridgeway Carriers – Driver Hiring Billboard</title>
<link href="https://fonts.googleapis.com/css2?family=Montserrat:wght@600;700;800&display=swap" rel="stylesheet">
<style>
  :root {
    --page: #ffffff;
    --board: #f1f1f1;
    --ink: #1e211d;
    --photo-dark: #1b2233;
    --photo-mid: #8d939c;
    --photo-light: #e4e5e7;
  }
  * { margin: 0; padding: 0; box-sizing: border-box; }
  html, body {
    width: 1200px;
    height: 1165px;
    overflow: hidden;
    background: var(--page);
    font-family: "Montserrat", Arial, sans-serif;
    color: var(--ink);
  }
  .billboard {
    position: absolute;
    left: 50px;
    top: 431px;
    width: 1100px;
    height: 303px;
    background: var(--board);
    box-shadow: 0 6px 28px rgba(0, 0, 0, 0.12);
    overflow: hidden;
  }
  .headline-lead {
    position: absolute;
    left: 60px;
    top: 34px;
    font-size: 37px;
    font-weight: 800;
    letter-spacing: 0.5px;
    line-height: 1;
  }
  .headline-amount {
    position: absolute;
    left: 58px;
    top: 78px;
    font-size: 82px;
    font-weight: 800;
    letter-spacing: -1px;
    line-height: 1;
  }
  .phone-box {
    position: absolute;
    left: 61px;
    top: 169px;
    width: 294px;
    height: 52px;
  }
  .phone-box svg { position: absolute; inset: 0; }
  .phone-number {
    position: absolute;
    inset: 0;
    display: flex;
    align-items: center;
    justify-content: center;
    font-size: 33px;
    font-weight: 800;
    letter-spacing: 0.3px;
  }
  .website {
    position: absolute;
    left: 88px;
    top: 240px;
    display: flex;
    align-items: center;
    gap: 10px;
    font-size: 16px;
    font-weight: 700;
  }
  .brand {
    position: absolute;
    right: 46px;
    top: 30px;
    display: flex;
    align-items: center;
    gap: 10px;
    font-size: 28px;
    font-weight: 800;
    text-transform: uppercase;
    letter-spacing: 0.5px;
  }
  .brand-mark {
    width: 22px;
    height: 22px;
    background: var(--ink);
  }
  .truck-photo {
    position: absolute;
    left: 438px;
    top: 80px;
    width: 606px;
    height: 204px;
    background: linear-gradient(100deg, var(--photo-light) 0%, var(--photo-mid) 25%, var(--photo-dark) 55%, var(--photo-dark) 85%, var(--photo-mid) 100%);
    border-radius: 4px;
  }
</style>
</head>
<body>
  <section class="billboard">
    <p class="headline-lead">MAKE UP TO</p>
    <p class="headline-amount">$90,000</p>

    <div class="phone-box">
      <svg width="294" height="52" viewBox="0 0 294 52" aria-hidden="true">
        <path d="M14 2 H292 V50 H2 V12 Z" fill="none" stroke="#1e211d" stroke-width="3"/>
      </svg>
      <span class="phone-number">803-555-0172</span>
    </div>

    <p class="website">
      <svg width="20" height="20" viewBox="0 0 24 24" aria-hidden="true" fill="none" stroke="#1e211d" stroke-width="1.6">
        <circle cx="11" cy="11" r="9"/>
        <ellipse cx="11" cy="11" rx="4" ry="9"/>
        <line x1="2" y1="11" x2="20" y2="11"/>
        <line x1="4" y1="6" x2="18" y2="6"/>
        <line x1="4" y1="16" x2="18" y2="16"/>
        <path d="M15 15 L23 19 L19 20 L20 24 Z" fill="#1e211d" stroke="none"/>
      </svg>
      ridgewaycarriers.com
    </p>

    <div class="brand">
      <span class="brand-mark"></span>
      <span class="brand-name">Ridgeway Carriers</span>
    </div>

    <div class="truck-photo" role="img" aria-label="Photo of a black semi truck pulling a flatbed trailer with a tarp-covered load"></div>
  </section>
</body>
</html>
```